Need a simple buisness card for my plumbing business. Would like it to be black background with white text.

Industry/Entity Type

Business

Requirements
Must have
• On the front of the card I need to have,
TKW PLUMBING SERVICES
PLUMBERS, DRAINERS & GASFITTERS
Dorian Lessop
0491576038
Info@tkwplumbingservices.com.au
LIC No 518047k
ABN No 57091836254
On the back I need in point form
Domestic,industrial,commercial, all new installations, renovations, sewer renewals, repairs,
Fully licensed and insured
Nice to have
• A nice simple logo

```html
<!DOCTYPE html>
<html lang="en">
<head>
<meta charset="utf-8">
<title>TKW Plumbing Services – Business Card</title>
<link href="https://fonts.googleapis.com/css2?family=Arimo:wght@400;700&display=swap" rel="stylesheet">
<style>
  :root {
    --page: #ffffff;
    --stage: #58595a;
    --card-dark: #141414;
    --card-dark-edge: #2a2a2a;
    --card-light: #ffffff;
    --ink-light: #ffffff;
    --ink-dark: #111111;
    --sub-light: #bdbdbd;
    --sub-dark: #555555;
    --swoosh: #e6e6e6;
  }
  html, body {
    margin: 0;
    padding: 0;
    width: 1200px;
    height: 791px;
    overflow: hidden;
    background: var(--page);
    font-family: "Arimo", Arial, sans-serif;
  }
  .stage {
    position: absolute;
    left: 0;
    top: 0;
    width: 1200px;
    height: 791px;
    background: var(--stage);
    border-radius: 27px;
  }
  .card {
    position: absolute;
    width: 442px;
    height: 265px;
    border-radius: 6px;
    overflow: hidden;
  }
  .card--front {
    left: 377px;
    top: 114px;
    background: var(--card-dark);
    border: 2px solid var(--card-dark-edge);
    box-sizing: border-box;
  }
  .card--back {
    left: 380px;
    top: 421px;
    background: var(--card-light);
  }
  .card__texture,
  .card__swoosh {
    position: absolute;
    left: 0;
    top: 0;
    width: 100%;
    height: 100%;
  }
  .brand-name {
    position: absolute;
    margin: 0;
    font-weight: 700;
    font-size: 30px;
    line-height: 1;
    letter-spacing: 0.2px;
    white-space: nowrap;
  }
  .brand-tagline {
    position: absolute;
    margin: 0;
    font-size: 12.5px;
    line-height: 1;
    letter-spacing: 1.6px;
    white-space: nowrap;
  }
  .card--front .brand-name { left: 21px; top: 47px; color: var(--ink-light); }
  .card--front .brand-tagline { left: 22px; top: 78px; color: var(--sub-light); }
  .card--back .brand-name { left: 17px; top: 15px; color: var(--ink-dark); }
  .card--back .brand-tagline { left: 18px; top: 46px; color: var(--sub-dark); }
  .contact {
    position: absolute;
    left: 21px;
    top: 146px;
    margin: 0;
    padding: 0;
    list-style: none;
    color: var(--ink-light);
    font-size: 17px;
    line-height: 21px;
  }
  .services {
    position: absolute;
    left: 36px;
    top: 112px;
    width: 380px;
    margin: 0;
    padding: 0 0 0 18px;
    box-sizing: border-box;
    display: grid;
    grid-template-columns: 1fr 1fr;
    column-gap: 30px;
    color: var(--ink-dark);
    font-size: 15.5px;
    line-height: 26px;
    list-style: disc;
  }
  .services li { white-space: nowrap; }
</style>
</head>
<body>
  <main class="stage">
    <section class="card card--front" aria-label="Business card front">
      <svg class="card__texture" role="img" aria-label="Dark textured card surface" viewBox="0 0 438 261" preserveAspectRatio="none">
        <defs>
          <linearGradient id="darkSurface" x1="0" y1="0" x2="1" y2="1">
            <stop offset="0" stop-color="#1c1c1c"/>
            <stop offset="0.5" stop-color="#121212"/>
            <stop offset="1" stop-color="#1a1a1a"/>
          </linearGradient>
        </defs>
        <rect width="438" height="261" fill="url(#darkSurface)"/>
      </svg>
      <h1 class="brand-name">TKW PLUMBING SERVICES</h1>
      <p class="brand-tagline">PLUMBERS, DRAINERS &amp; GASFITTERS</p>
      <ul class="contact">
        <li>Dorian Lessop</li>
        <li>0491576038</li>
        <li>Info@tkwplumbingservices.com.au</li>
        <li>Lic no: 518047k</li>
        <li>ABN no: 57091836254</li>
      </ul>
    </section>

    <section class="card card--back" aria-label="Business card back">
      <svg class="card__swoosh" role="img" aria-label="Faint swoosh decoration" viewBox="0 0 442 265" preserveAspectRatio="none">
        <defs>
          <linearGradient id="softSwoosh" x1="0" y1="0" x2="1" y2="1">
            <stop offset="0" stop-color="#ffffff"/>
            <stop offset="0.5" stop-color="#eeeeee"/>
            <stop offset="1" stop-color="#f6f6f6"/>
          </linearGradient>
        </defs>
        <rect width="442" height="265" fill="url(#softSwoosh)"/>
      </svg>
      <h2 class="brand-name">TKW PLUMBING SERVICES</h2>
      <p class="brand-tagline">PLUMBERS, DRAINERS &amp; GASFITTERS</p>
      <ul class="services">
        <li>Domestic</li>
        <li>Industrial</li>
        <li>Commercial</li>
        <li>All new installations</li>
        <li>Renovations</li>
        <li>Sewer renewals</li>
        <li>Repairs</li>
        <li>Fully licensed and insured</li>
      </ul>
    </section>
  </main>
</body>
</html>
```